Fun relaxed Travel Photography Business Card*

Require a fun, funky and quirky but rememberable business card for a travel photographer

Industry/Entity Type

Photographer

Contact Information for Business Card

Front Card

(my name) Dane M.

Travel Photographer ( small under travel photographer) “self-proclaimed”

(website logo) wanderingsofdane.example

(Instagram logo) @wanderings_of_dane

(Instagram logo) @wanderings_of_dane_2.0 (backup for when Instagram puts Dane on timeout for bad behaviour)

Tel: N/A (removing the potential awkwardness of me not replying)

Email: (see above)

Back Card

Offending people since 1986

(Bottom right corner) “p.s. travelling made me fatTER”

Font styles to use
Serif

Colors

Designer to choose colors to be used in the design.

Requirements
Must have
• a camera
• a similar cartoon version of me as the "logo" see attached files, try to make as similar as possible

```html
<!DOCTYPE html>
<html lang="en">
<head>
<meta charset="utf-8">
<title>Dane M. – Travel Photographer Business Card</title>
<link rel="stylesheet" href="https://fonts.googleapis.com/css2?family=Raleway:wght@400;500;700&display=swap">
<style>
  :root {
    --page-bg: #2b2e34;
    --card-blue: #3f6289;
    --card-blue-light: #4a6f98;
    --card-white: #ffffff;
    --divider-grey: #7d7f82;
    --text-light: #e9eef4;
    --text-blue: #3f6289;
    --portrait-dark: #3a2a20;
  }
  * { box-sizing: border-box; margin: 0; padding: 0; }
  html, body {
    width: 1200px; height: 900px; overflow: hidden;
    background: var(--page-bg);
    font-family: "Raleway", sans-serif;
  }
  .sheet {
    width: 1200px; height: 900px;
    display: flex; flex-direction: column; align-items: center; justify-content: center;
    gap: 40px;
  }
  .card {
    position: relative;
    width: 700px; height: 400px;
    overflow: hidden;
    border-radius: 4px;
  }

  /* Front */
  .card--front { background: var(--card-white); }
  .card--front .info-band {
    position: absolute; left: 0; right: 0; top: 240px; bottom: 0;
    background: linear-gradient(180deg, var(--card-blue-light), var(--card-blue));
  }
  .card--front .divider {
    position: absolute; left: 0; right: 0; top: 234px; height: 3px;
    background: var(--divider-grey);
  }
  .logo-art {
    position: absolute;
    border-radius: 22px;
  }
  .card--front .logo-art {
    left: 450px; top: 58px; width: 190px; height: 176px;
    background: linear-gradient(135deg, var(--card-blue) 0%, var(--card-blue) 55%, var(--portrait-dark) 100%);
  }
  .contact-list {
    position: absolute; left: 34px; top: 262px;
    list-style: none;
    color: var(--text-light);
    font-size: 16px; line-height: 28px; font-weight: 400;
  }
  .contact-list li { display: flex; align-items: center; gap: 10px; }
  .contact-list svg { width: 16px; height: 16px; flex: none; }
  .identity {
    position: absolute; right: 40px; top: 268px;
    color: var(--text-light);
    text-align: left;
  }
  .identity .name-line { display: flex; align-items: center; gap: 12px; }
  .identity .name { font-size: 24px; font-weight: 700; }
  .identity .bar { width: 2px; height: 28px; background: var(--text-light); }
  .identity .role { font-size: 19px; font-weight: 500; }
  .identity .qualifier { font-size: 16px; margin-top: 4px; padding-left: 120px; }

  /* Back */
  .card--back { background: linear-gradient(180deg, var(--card-blue), var(--card-blue-light)); }
  .card--back .stripe {
    position: absolute; left: 0; right: 0; top: 250px; height: 50px;
    background: var(--card-white);
  }
  .card--back .logo-art {
    left: 260px; top: 64px; width: 200px; height: 186px;
    background: linear-gradient(135deg, var(--card-white) 0%, var(--card-white) 50%, var(--portrait-dark) 100%);
  }
  .tagline {
    position: absolute; left: 0; right: 0; text-align: center;
  }
  .tagline--main { top: 262px; color: var(--text-blue); font-size: 19px; font-weight: 500; padding-left: 60px; }
  .tagline--ps { top: 318px; color: var(--text-light); font-size: 19px; font-weight: 400; padding-left: 60px; }
</style>
</head>
<body>
<main class="sheet">

  <section class="card card--front" aria-label="Business card front">
    <div class="logo-art" role="img" aria-label="Camera-shaped logo framing a cartoon portrait of Dane in sunglasses and a floral shirt"></div>
    <div class="divider"></div>
    <div class="info-band"></div>

    <ul class="contact-list">
      <li>
        <svg viewBox="0 0 16 16" aria-hidden="true"><rect x="1.5" y="1.5" width="13" height="13" rx="3" fill="none" stroke="currentColor" stroke-width="1.6"/></svg>
        @wanderings_of_dane
      </li>
      <li>
        <svg viewBox="0 0 16 16" aria-hidden="true"><rect x="1.5" y="1.5" width="13" height="13" rx="3" fill="none" stroke="currentColor" stroke-width="1.6"/></svg>
        @wanderings_of_dane_2.0
      </li>
      <li>
        <svg viewBox="0 0 16 16" aria-hidden="true"><rect x="1" y="3" width="14" height="10" rx="1" fill="none" stroke="currentColor" stroke-width="1.5"/><path d="M1.5 3.8 8 9l6.5-5.2" fill="none" stroke="currentColor" stroke-width="1.5"/></svg>
        danes.wanderings@example.com
      </li>
      <li>
        <svg viewBox="0 0 16 16" aria-hidden="true"><circle cx="8" cy="8" r="6.5" fill="none" stroke="currentColor" stroke-width="1.4"/><ellipse cx="8" cy="8" rx="3" ry="6.5" fill="none" stroke="currentColor" stroke-width="1.2"/><path d="M1.5 8h13" stroke="currentColor" stroke-width="1.2"/></svg>
        wanderingsofdane.example
      </li>
    </ul>

    <div class="identity">
      <div class="name-line">
        <span class="name">Dane M.</span>
        <span class="bar"></span>
        <span class="role">Travel Photographer</span>
      </div>
      <div class="qualifier">self-proclaimed</div>
    </div>
  </section>

  <section class="card card--back" aria-label="Business card back">
    <div class="stripe"></div>
    <div class="logo-art" role="img" aria-label="Camera-shaped logo framing a cartoon portrait of Dane in sunglasses and a floral shirt"></div>
    <p class="tagline tagline--main">Offending people since 1986</p>
    <p class="tagline tagline--ps">p.s. travelling made me fatTER</p>
  </section>

</main>
</body>
</html>
```